Dorsey K. Wendell Business Card

We need a business card for our company Dorsey K. Wendell Heating & Plumbing to be distributed to potential customers. It should follow the color scheme of our logo and have a modern upscale and masculine look.

The logo is attached and the info below should also be included:

5187 W. Cedar Brook Rd.
Larkfield, PA 10000

Russell T. Wendell
(555) 592-0817
russelltwendell@fernmail.net
dorseykwendell.net
PA #093148

Industry/Entity Type

Business

Contact Information for Business Card

5187 W. Cedar Brook Rd.
Larkfield, PA 10000

Russell T. Wendell
(555) 592-0817
russelltwendell@fernmail.net
dorseykwendell.net
PA #093148

Colors

Designer to choose colors to be used in the design.

Requirements
Must have
• Information above included

```html
<!DOCTYPE html>
<html lang="en">
<head>
<meta charset="utf-8">
<title>Dorsey K. Wendell Business Card</title>
<link rel="stylesheet" href="https://fonts.googleapis.com/css2?family=Roboto:wght@400;700&family=Open+Sans:wght@500&display=swap">
<style>
  :root {
    --brand-blue: #0555a0;
    --brand-green: #a6cf38;
    --card-white: #f4f4f4;
    --ink: #1a1a1a;
    --page: #e6e6e6;
  }
  * { margin: 0; padding: 0; box-sizing: border-box; }
  html, body { width: 1200px; height: 1200px; overflow: hidden; }
  body {
    background: var(--page);
    font-family: "Roboto", Arial, sans-serif;
    display: flex;
    flex-direction: column;
    align-items: center;
    justify-content: center;
    gap: 60px;
  }
  .card {
    position: relative;
    width: 900px;
    height: 514px;
    overflow: hidden;
  }
  .card-front { background: var(--brand-blue); }
  .front-name {
    position: absolute;
    left: 50px;
    bottom: 62px;
    color: #fff;
    font-weight: 700;
    font-size: 34px;
  }
  .card-back { background: var(--card-white); }
  .brand {
    position: absolute;
    left: 51px;
    top: 212px;
    display: flex;
    align-items: center;
    gap: 14px;
  }
  .brand-square {
    width: 44px;
    height: 44px;
    background: var(--brand-blue);
  }
  .brand-name {
    color: var(--brand-blue);
    font-weight: 700;
    font-size: 33px;
    white-space: nowrap;
  }
  .contact-list {
    position: absolute;
    left: 478px;
    top: 160px;
    list-style: none;
  }
  .contact-item {
    display: flex;
    align-items: center;
    height: 51px;
    font-size: 25px;
    color: var(--ink);
    white-space: nowrap;
  }
  .contact-item svg {
    width: 24px;
    height: 24px;
    margin-right: 20px;
    flex: none;
    fill: none;
    stroke: var(--brand-blue);
    stroke-width: 2;
  }
  .contact-name { font-weight: 700; font-size: 27px; }
  .footer-band {
    position: absolute;
    left: 0;
    bottom: 0;
    width: 100%;
    height: 49px;
    display: flex;
    font-family: "Open Sans", Arial, sans-serif;
    font-weight: 500;
    font-size: 24px;
    letter-spacing: 1px;
    white-space: nowrap;
  }
  .footer-address {
    width: 668px;
    background: var(--brand-blue);
    color: #fff;
    display: flex;
    align-items: center;
    padding-left: 50px;
  }
  .footer-license {
    flex: 1;
    background: var(--brand-green);
    color: var(--ink);
    display: flex;
    align-items: center;
    padding-left: 28px;
  }
</style>
</head>
<body>
  <section class="card card-front">
    <div class="front-name">Dorsey K. Wendell</div>
  </section>

  <section class="card card-back">
    <div class="brand">
      <span class="brand-square"></span>
      <span class="brand-name">Dorsey K. Wendell</span>
    </div>

    <ul class="contact-list">
      <li class="contact-item contact-name">
        <svg viewBox="0 0 24 24"><circle cx="12" cy="7" r="4" fill="var(--brand-blue)" stroke="none"/><path d="M4 21c0-5 4-8 8-8s8 3 8 8z" fill="var(--brand-blue)" stroke="none"/></svg>
        Russell T. Wendell
      </li>
      <li class="contact-item">
        <svg viewBox="0 0 24 24"><path d="M6.6 3.5l3 3.2-1.8 2.4c1.2 2.6 3.4 4.8 6 6l2.4-1.8 3.2 3-1.6 3.2C11 19 5 13 3.5 5.1z" fill="var(--brand-blue)" stroke="none"/></svg>
        (555) 592-0817
      </li>
      <li class="contact-item">
        <svg viewBox="0 0 24 24"><path d="M3 10l9-6 9 6v10H3z"/><path d="M3 10l9 6 9-6"/></svg>
        russelltwendell@fernmail.net
      </li>
      <li class="contact-item">
        <svg viewBox="0 0 24 24"><circle cx="12" cy="12" r="9"/><ellipse cx="12" cy="12" rx="4" ry="9"/><path d="M3 12h18M5 7h14M5 17h14"/></svg>
        dorseykwendell.net
      </li>
    </ul>

    <div class="footer-band">
      <div class="footer-address">5187 W. Cedar Brook Rd, Larkfield, PA 10000</div>
      <div class="footer-license">PA #093148</div>
    </div>
  </section>
</body>
</html>
```